Business card for new speaking/consulting business
Carla Venhuizen, CRBTEQ
Bright & Fun-filled
Growth Mentor, Billing Workflow Advisor, Keynote Host
Elmsworth, CO
carla.venhuizen@postvexa.com

```html
<!DOCTYPE html>
<html lang="en">
<head>
<meta charset="utf-8">
<title>Carla Venhuizen – Business Card</title>
<link rel="stylesheet" href="https://fonts.googleapis.com/css2?family=Open+Sans:wght@400;600;700&display=swap">
<style>
  :root {
    --page-bg: #e9e7e3;
    --card-white: #ffffff;
    --brand-blue: #1f9bd7;
    --light-blue: #6cc4ec;
    --lime: #8cc63f;
    --light-lime: #c4e27c;
    --text-white: #ffffff;
  }
  * { margin: 0; padding: 0; box-sizing: border-box; }
  html, body {
    width: 1200px;
    height: 900px;
    overflow: hidden;
    background: var(--page-bg);
    font-family: "Open Sans", Arial, sans-serif;
  }
  .business-card {
    position: absolute;
    left: 100px;
    top: 164px;
    width: 1000px;
    height: 572px;
    background: var(--card-white);
    overflow: hidden;
    box-shadow: 0 10px 30px rgba(0,0,0,0.18);
  }
  .wave-art {
    position: absolute;
    inset: 0;
    width: 100%;
    height: 100%;
  }
  .brand-name {
    position: absolute;
    left: 470px;
    top: 92px;
    display: flex;
    align-items: center;
    gap: 16px;
    color: var(--brand-blue);
    font-weight: 600;
    font-size: 44px;
    letter-spacing: 3px;
    white-space: nowrap;
  }
  .brand-dot {
    width: 30px;
    height: 30px;
    border-radius: 50%;
    background: var(--brand-blue);
    flex: none;
  }
  .contact-list {
    position: absolute;
    left: 30px;
    top: 390px;
    list-style: none;
    color: var(--text-white);
    font-size: 18px;
    line-height: 1;
  }
  .contact-item {
    display: flex;
    align-items: center;
    gap: 10px;
    height: 34px;
  }
  .contact-icon {
    width: 22px;
    height: 22px;
    flex: none;
  }
  .person {
    position: absolute;
    right: 40px;
    top: 426px;
    text-align: right;
    color: var(--text-white);
    white-space: nowrap;
  }
  .person-name {
    font-weight: 700;
    font-size: 20px;
    margin-bottom: 14px;
  }
  .person-roles {
    font-size: 16px;
  }
</style>
</head>
<body>
  <div class="business-card">
    <svg class="wave-art" viewBox="0 0 1000 572" preserveAspectRatio="none" aria-hidden="true">
      <path d="M0,300 C220,330 420,200 640,200 C800,200 900,170 1000,150 L1000,572 L0,572 Z" fill="var(--light-lime)"/>
      <path d="M0,318 C230,350 430,222 650,222 C810,222 905,195 1000,178 L1000,572 L0,572 Z" fill="var(--lime)"/>
      <path d="M0,336 C240,372 440,246 660,246 C815,246 910,222 1000,206 L1000,572 L0,572 Z" fill="var(--card-white)"/>
      <path d="M0,352 C240,390 450,266 670,266 C820,266 912,244 1000,230 L1000,572 L0,572 Z" fill="var(--light-blue)"/>
      <path d="M0,366 C250,400 460,285 680,285 C830,285 915,266 1000,254 L1000,572 L0,572 Z" fill="var(--brand-blue)"/>
    </svg>

    <div class="brand-name"><span class="brand-dot"></span>CARLA VENHUIZEN</div>

    <ul class="contact-list">
      <li class="contact-item">
        <svg class="contact-icon" viewBox="0 0 22 22"><circle cx="11" cy="11" r="11" fill="#fff"/><path d="M11 5a4 4 0 0 0-4 4c0 3 4 8 4 8s4-5 4-8a4 4 0 0 0-4-4zm0 5.5a1.5 1.5 0 1 1 0-3 1.5 1.5 0 0 1 0 3z" fill="var(--brand-blue)"/></svg>
        <span>Elmsworth, CO</span>
      </li>
      <li class="contact-item">
        <svg class="contact-icon" viewBox="0 0 22 22"><circle cx="11" cy="11" r="11" fill="#fff"/><path d="M8 5.5l2 3-1.3 1.3a7 7 0 0 0 3.5 3.5l1.3-1.3 3 2-1.2 2c-4 .3-9-4.7-8.7-8.7z" fill="var(--brand-blue)"/></svg>
        <span>(303) 555-0147</span>
      </li>
      <li class="contact-item">
        <svg class="contact-icon" viewBox="0 0 22 22"><circle cx="11" cy="11" r="11" fill="#fff"/><rect x="5.5" y="7" width="11" height="8" fill="var(--brand-blue)"/><path d="M5.5 7l5.5 4.5L16.5 7" fill="none" stroke="#fff" stroke-width="1.2"/></svg>
        <span>carla.venhuizen@postvexa.com</span>
      </li>
      <li class="contact-item">
        <svg class="contact-icon" viewBox="0 0 22 22"><circle cx="11" cy="11" r="11" fill="#fff"/><g fill="none" stroke="var(--brand-blue)" stroke-width="1.3"><circle cx="11" cy="11" r="6"/><ellipse cx="11" cy="11" rx="2.6" ry="6"/><path d="M5 11h12"/></g></svg>
        <span>www.venhuizencoaching.com</span>
      </li>
    </ul>

    <div class="person">
      <p class="person-name">Carla Venhuizen, CRBTEQ</p>
      <p class="person-roles">Growth Mentor, Billing Workflow Advisor, Keynote Host</p>
    </div>
  </div>
</body>
</html>
```